Wordpress Theme for Medical Clinics

** Please view updated Sitemap2.pdf doc to clarify some confusion ***

This is a multiuser WordPress subscription site for medical clinics. Please see attachment for sitemap. Please do not include extra content like social media icons, search bars, or images. If you have questions, please ask for clarification.
The site contains the following pages and sub-pages:

1. Home
2. Our Clinic
2a. Our Clinic > Mission
2b. Our Clinic > Services
2c. Our Clinic > Clinic Policies
2d. Our Clinic > Schedules
3. Our Staff
3a. Our Staff > [Staff member page]
4. Resources
4a. Resources > Patient Health (index)
4b. Resources > Patient Health (index) > [post]
4c. Resources > Links
4d. Resources > Forms
5. Alerts
5a. Alerts > [Alert Page]
6. Contact Us

Includes the Following Pages, Subpages, and Content
1. Home
a. About Us
b. Our Staff
c. Bulletins
d. Accepting New Patients (shown as an alert widget)
e. Links
i. Physician Toolbox
ii. Book an Appointment
f. Clinic Policies
i. Show first 3 policies (e.g. Late Arrivals, Missed Appointments, Fees)
ii. Link to Clinic Policies page
g. Primary widget (displayed on all pages)
i. Hours of operation
ii. Contact Info
1. Tel
2. Fax
3. Email
4. Address
5. Get directions (link to Google Maps)
2. Our Clinic
a. Main Page
i. Clinic Name
ii. Overview
iii. Languages Spoken
iv. Secondary Navigation
1. Mission
2. Services
3. Clinic Policies
4. Schedules (see attachment)
b. Our Clinic > Mission
c. Our Clinic > Services
i. For each service include service TITLE and DESCRIPTION
d. Our Clinic > Clinic Policies
i. For each policy include policy TITLE and DESCRIPTION
ii. Include the following policies in mockup
1. Late arrivals
2. Missed appointments
3. Fees for missed appointments
4. Referrals and follow-ups
5. Services not covered by RDV
6. Information for TQL patients
7. Medical Legal Reports
e. Our Clinic > Schedules
3. Our Staff
a. Main Page
i. Display a list of staff members. Include NAME and DESIGNATION
b. Our Staff > [Staff Name]
i. Include NAME, PICTURE, DESIGNATION, and BIO
4. Resources
a. Resources > Patient Health
i. Main Page
1. Posts (ordered by date)
a. Title
b. Summary
2. Side Navigation
a. Post Categories
ii. Patient Health > [post title]
1. Title
2. Post Category
3. Date
4. Author
5. Summary
6. Body
b. Resources > Links
1. Secondary Navigation - Categories
a. Sample Categories:
i. Local Services
ii. RDV and Drug Coverage
iii. Mental Health Resources
2. Category page
a. Include the following links in the 'Local Services' category
i. Hypertension clinics
ii. Home Care services
iii. Vaccine Clinics
c. Resources > Forms
i. Display a table with form TITLE and CATEGORY
ii. Side Navigation
1. Form Categories
a. Use the following sample Categories
i. Referrals
ii. Insurance
iii. Intake
iv. Discharge
v. Waivers
5. Alerts
a. Main page
i. List of all Alert posts
1. Include post TITLE as a link to the post
ii. Side Navigation
1. Alerts Archive
a. shown as Month + Number of posts
iii. Alerts > [Alert page]
1. Include TITLE, DATE, AUTHOR, BODY
6. Contact Us
a. Map
b. Hours of operation
c. Address
d. Phone number
e. Fax number
e. Fax number
f. Map
g. Email

Design notes:
- fixed width
- responsive (need designs for mobile, tablet, and desktop)
- simple, dark font, white background
- use Font Awesome icons where needed
- user adds own logo

Target Market(s)

Medical Clinics

Industry/Entity Type

Medical

Number of Pages Required

5+ page

Font styles to use
Serif
Sans Serif

Requirements
Must have
• Please keep designs very simple.
• Examples:
• https://www.quandrix.com/install
• http://www.tervolane.com/company/about-us
• http://brightnumberhub.org/
• http://www.vorn.com/
Should not have
• Minimal or no use of shadows and gradients

```html
<!DOCTYPE html>
<html lang="en">
<head>
<meta charset="utf-8">
<title>Harbor Clinic</title>
<link href="https://fonts.googleapis.com/css2?family=Raleway:wght@500;600;700&family=Arimo:wght@400;700&display=swap" rel="stylesheet">
<style>
:root{
  --blue:#16689a;
  --blue-dark:#1f5d85;
  --ink:#333;
  --muted:#555;
  --dark:#2b2b2b;
  --footer:#3d3d3d;
  --panel:#4a4a4a;
  --light:#f1f1f2;
  --white:#fff;
}
*{margin:0;padding:0;box-sizing:border-box}
html,body{width:760px;height:1200px;overflow:hidden}
body{position:relative;font-family:"Arimo",Arial,sans-serif;color:var(--ink);background:var(--white);font-size:9px}
.abs{position:absolute}
ul{list-style:none}
a{color:inherit}
.h-raleway{font-family:"Raleway",Arial,sans-serif}

.topbar{left:0;top:0;width:760px;height:30px;background:var(--dark);color:#eee;font-size:8.5px}
.topbar .contact{left:64px;top:10px}
.topbar .quick{right:63px;top:10px}

.header{left:0;top:30px;width:760px;height:52px;background:var(--white);border-bottom:1px solid #ddd}
.brand{left:70px;top:12px;display:flex;align-items:center;gap:8px;font-family:"Raleway",sans-serif;font-weight:500;font-size:24px;color:var(--blue)}
.brand .dot{width:16px;height:16px;border-radius:50%;background:var(--blue)}
.nav{left:287px;top:0;height:52px;display:flex;font-size:8.6px;color:#222}
.nav li{padding:0 11px;line-height:52px;margin-right:8px}
.nav li.current{background:#f4f4f4;border-bottom:3px solid var(--blue);line-height:50px}

.hero{left:0;top:82px;width:760px;height:276px;background:linear-gradient(100deg,#e6ecef 0%,#f3efe9 45%,#e9d8c6 75%,#c9b29a 100%)}
.hero .arrow{top:99px}
.hero .caption{left:64px;top:198px;width:633px;height:64px;background:rgba(255,255,255,.78);border-left:5px solid var(--blue);padding:10px 14px;font-size:8.8px;line-height:13.8px;color:#444}

.about{left:0;top:358px;width:760px;height:198px;background:var(--blue);color:var(--white)}
.about h2{left:64px;top:26px;font-family:"Raleway",sans-serif;font-weight:600;font-size:15px}
.about .rule{left:160px;top:34px;width:300px;height:1px;background:rgba(255,255,255,.35)}
.about .photo{left:64px;top:58px;width:150px;height:114px;border:2px solid var(--white);background:linear-gradient(135deg,#e9eef1,#c9d3d9)}
.about .text{left:230px;top:58px;width:240px;font-weight:700;font-size:9px;line-height:12.8px;letter-spacing:.1px}
.about .text p+p{margin-top:12px}
.hours{left:500px;top:17px;width:189px;height:173px;border:1px solid rgba(255,255,255,.35)}
.hours h3{left:15px;top:8px;font-family:"Raleway",sans-serif;font-weight:500;font-size:15px}
.hours table{left:15px;top:40px;font-size:8.3px;border-collapse:collapse}
.hours td{height:15.2px;padding:0}
.hours td:first-child{width:82px}
.hours .more{left:15px;top:144px;text-decoration:underline;font-size:8.3px}

.directory{left:0;top:556px;width:760px;height:158px;background:var(--light)}
.directory h2{font-family:"Raleway",sans-serif;font-weight:500;font-size:15px;color:var(--blue-dark)}
.directory .rule{height:1px;background:#c9c9c9;width:88px}
.directory ul{font-size:10.4px;color:#444}
.directory li{height:19px;padding-left:13px;position:relative}
.directory li::before{content:"→";position:absolute;left:0;top:0;font-size:9px}
.contact-table{font-size:10.4px;color:#333;border-collapse:collapse}
.contact-table td{vertical-align:top;padding:0 0 4px}
.contact-table td:first-child{width:86px;padding-left:13px;position:relative}
.contact-table td:first-child::before{content:"→";position:absolute;left:0;font-size:9px}

.alerts h2{left:67px;top:742px;font-family:"Raleway",sans-serif;font-weight:500;font-size:15px;color:var(--blue-dark)}
.alert{width:385px}
.alert h4{font-size:9px;font-weight:700;color:#333;margin-bottom:5px}
.alert p{font-size:8.8px;line-height:12.8px;color:#555}
.alert .read{display:block;margin-top:5px;color:var(--blue);text-decoration:none}
.alert-divider{left:68px;top:856px;width:382px;height:1px;background:#ddd}
.new-patients{left:498px;top:745px;width:199px;height:57px;background:var(--panel);border:3px solid #9b9b9b;color:var(--white);padding:8px 19px}
.new-patients h3{font-family:"Raleway",sans-serif;font-weight:600;font-size:15px;margin-bottom:5px}
.new-patients p{font-size:8.6px}
.new-patients a{text-decoration:underline}
.policies h3{left:498px;top:822px;font-family:"Raleway",sans-serif;font-weight:500;font-size:16px;color:var(--blue-dark)}
.policies ul{left:499px;top:850px;font-size:8.8px;color:#444}
.policies li{height:15.9px;padding-left:13px;position:relative}
.policies li::before{content:"→";position:absolute;left:0;font-size:8px}

.footer{left:0;top:990px;width:760px;height:180px;background:var(--footer);color:var(--white)}
.footer h3{font-family:"Raleway",sans-serif;font-weight:700;font-size:16px}
.footer ul{font-size:8.8px;margin-top:6px}
.footer li{height:15.2px;padding-left:12px;position:relative}
.footer li::before{content:"";position:absolute;left:2px;top:3px;border-left:3px solid #fff;border-top:2.5px solid transparent;border-bottom:2.5px solid transparent}
.footer table{font-size:8.8px;border-collapse:collapse;margin-top:6px}
.footer td{height:15.2px;padding:0}
.footer td:first-child{width:84px}
.footer .more{text-decoration:underline;font-size:8.8px}
.footer .row{display:flex;gap:12px;font-size:8.8px;margin-bottom:9px}
.footer .row svg{flex:none}
.bottombar{left:0;top:1170px;width:760px;height:30px;background:var(--blue);color:var(--white);font-size:8.8px;text-align:center;line-height:30px}
</style>
</head>
<body>

<div class="abs topbar">
  <div class="abs contact">Telephone 0321000111 &nbsp;|&nbsp; Email info@harborclinic.com</div>
  <div class="abs quick">Book an Appointment &nbsp;&nbsp;|&nbsp;&nbsp; Physician Toolbar</div>
</div>

<header class="abs header">
  <div class="abs brand"><span class="dot"></span>Harbor Clinic</div>
  <ul class="abs nav">
    <li class="current">HOME</li><li>OUR CLINIC</li><li>STAFF</li><li>RESOURCES</li><li>ALERTS</li><li>CONTACT US</li>
  </ul>
</header>

<section class="abs hero" role="img" aria-label="Photo of a doctor with a stethoscope examining a smiling baby held by its mother">
  <svg class="abs arrow" style="left:20px" width="28" height="28" viewBox="0 0 28 28"><circle cx="14" cy="14" r="12" fill="none" stroke="#777" stroke-width="2.4"/><path d="M16 8l-6 6 6 6" fill="none" stroke="#777" stroke-width="2.4"/></svg>
  <svg class="abs arrow" style="left:715px" width="28" height="28" viewBox="0 0 28 28"><circle cx="14" cy="14" r="12" fill="none" stroke="#888" stroke-width="2.4"/><path d="M12 8l6 6-6 6" fill="none" stroke="#888" stroke-width="2.4"/></svg>
  <div class="abs caption">Lorem Ipsum is simply dummy text of the printing and typesetting industry. Lorem Ipsum has been the industry's standard dummy text ever since the 1500s, when an unknown printer took a galley of type and scrambled it to make.It has survived not only five centuries, but also the leap into electronic typesetting, remaining essentially unchanged. It was popularised in the 1960.</div>
</section>

<section class="abs about">
  <h2 class="abs">OUR CLINIC</h2>
  <div class="abs rule"></div>
  <div class="abs photo" role="img" aria-label="Photo of a doctor in a white coat holding a clipboard"></div>
  <div class="abs text">
    <p>Lorem Ipsum is simply dummy text of the printing and typesetting industry. Lorem Ipsum has been the industry's standard dummy text ever since the 1500s, when an unknown printer took a galley of type and scrambled it to make.</p>
    <p>It has survived not only five centuries, but also the leap into electronic typesetting, remaining essentially unchanged. It was popularised in the 1960.</p>
  </div>
  <div class="abs hours">
    <h3 class="abs">Hours of Operation</h3>
    <table class="abs">
      <tr><td>Monday</td><td>8:00 AM - 6:00 PM</td></tr>
      <tr><td>Tusday</td><td>8:00 AM - 6:00 PM</td></tr>
      <tr><td>Wednesday</td><td>8:00 AM - 6:00 PM</td></tr>
      <tr><td>Thursday</td><td>8:00 AM - 6:00 PM</td></tr>
      <tr><td>Friday</td><td>8:00 AM - 6:00 PM</td></tr>
      <tr><td>Saturday</td><td>8:00 AM - 4:00 PM</td></tr>
      <tr><td>Sunday</td><td>8:00 AM - 4:00 PM</td></tr>
    </table>
    <a class="abs more">Holiday hours</a>
  </div>
</section>

<section class="abs directory">
  <h2 class="abs" style="left:64px;top:24px">STAFF</h2>
  <div class="abs rule" style="left:119px;top:34px"></div>
  <ul class="abs" style="left:64px;top:56px">
    <li>Dr Alan Mercer MD</li><li>Dr Nora Vale MD</li><li>Dr Owen Hartley MD</li><li>Dr Ivan Rook MD</li>
  </ul>
  <h2 class="abs" style="left:282px;top:26px">LINKS</h2>
  <div class="abs rule" style="left:339px;top:36px"></div>
  <ul class="abs" style="left:282px;top:58px">
    <li>Dr Alan Mercer MD</li><li>Dr Nora Vale MD</li><li>Dr Owen Hartley MD</li><li>Dr Ivan Rook MD</li>
  </ul>
  <h2 class="abs" style="left:495px;top:27px">CONTACT</h2>
  <div class="abs rule" style="left:574px;top:37px"></div>
  <table class="abs contact-table" style="left:497px;top:59px">
    <tr><td>Telephone</td><td>8045550199</td></tr>
    <tr><td>Email</td><td>info@harborclinic.com</td></tr>
    <tr><td>Address</td><td style="line-height:16.6px">48 Cedar Lane<br>Lakeview B.C<br>Canada V2B4DF</td></tr>
  </table>
</section>

<section class="alerts">
  <h2 class="abs">ALERTS</h2>
  <article class="abs alert" style="left:68px;top:777px">
    <h4>Alert Headline 1</h4>
    <p>Lorem ipsum dolor sit amet, consectetuer adipiscing elit, sed diam nonummy nibh euismod tincidunt ut laoreet dolore dolor sit amet, consectetuer adipiscing elit, sed diam nonummy nibh euismod tincidunt ut laoreet dolore magna aliquam erat volutpat.</p>
    <a class="read">→ Read More</a>
  </article>
  <div class="abs alert-divider"></div>
  <article class="abs alert" style="left:70px;top:875px">
    <h4>Alert Headline 1</h4>
    <p>Lorem ipsum dolor sit amet, consectetuer adipiscing elit, sed diam nonummy nibh euismod tincidunt ut laoreet dolore dolor sit amet, consectetuer adipiscing elit, sed diam nonummy nibh euismod tincidunt ut laoreet dolore magna aliquam erat volutpat.</p>
    <a class="read">→ Read More</a>
  </article>
</section>

<aside class="abs new-patients">
  <h3>New Patients</h3>
  <p>Accepting new patients. <a>contact us</a></p>
</aside>

<aside class="policies">
  <h3 class="abs">Clinic Policies</h3>
  <ul class="abs">
    <li>Late Arrivals</li><li>Missed Appointments</li><li>Fees for Missed Appointment</li><li>Referrals and follow ups</li><li>Services not covered by RDV</li><li>Information for TQL Patients</li><li>Medicial Legal Reports</li>
  </ul>
</aside>

<footer class="abs footer">
  <div class="abs" style="left:72px;top:14px">
    <h3>Our Clinic</h3>
    <ul><li>Mission</li><li>Services</li><li>Schdules</li><li>Polices</li><li>Staff</li><li>Alerts</li><li>Contact us</li></ul>
  </div>
  <div class="abs" style="left:194px;top:14px">
    <h3>Resources</h3>
    <ul><li>Our &nbsp;Clinic</li><li>Mission</li><li>Services</li></ul>
  </div>
  <div class="abs" style="left:326px;top:13px">
    <h3>Hours Of Oprations</h3>
    <table>
      <tr><td>Monday</td><td>8:00 AM - 6:00 PM</td></tr>
      <tr><td>Tusday</td><td>8:00 AM - 6:00 PM</td></tr>
      <tr><td>Wednesday</td><td>8:00 AM - 6:00 PM</td></tr>
      <tr><td>Thursday</td><td>8:00 AM - 6:00 PM</td></tr>
      <tr><td>Friday</td><td>8:00 AM - 6:00 PM</td></tr>
      <tr><td>Satarday</td><td>8:00 AM - 4:00 PM</td></tr>
      <tr><td>Sunday</td><td>8:00 AM - 4:00 PM</td></tr>
    </table>
    <a class="more">Holiday hours</a>
  </div>
  <div class="abs" style="left:551px;top:13px">
    <h3 style="margin-bottom:14px">Contact us</h3>
    <div class="row"><svg width="12" height="12" viewBox="0 0 24 24"><path fill="#fff" d="M6.6 10.8a15 15 0 006.6 6.6l2.2-2.2c.3-.3.7-.4 1-.2 1.1.4 2.3.6 3.6.6.6 0 1 .4 1 1V20c0 .6-.4 1-1 1A17 17 0 013 4c0-.6.4-1 1-1h3.5c.6 0 1 .4 1 1 0 1.2.2 2.4.6 3.6.1.3 0 .7-.2 1z"/></svg><span style="margin-left:4px">8045550199</span></div>
    <div class="row"><svg width="14" height="11" viewBox="0 0 14 11"><rect x="0.5" y="0.5" width="13" height="10" fill="#fff"/><path d="M1 1l6 5 6-5M1 10l4.5-4.5M13 10L8.5 5.5" fill="none" stroke="#3d3d3d" stroke-width="1.2"/></svg><span style="margin-left:2px">info@harborclinic.com</span></div>
    <div class="row"><svg width="12" height="15" viewBox="0 0 12 15"><path fill="#fff" d="M6 0a6 6 0 00-6 6c0 4.5 6 9 6 9s6-4.5 6-9a6 6 0 00-6-6zm0 8.5A2.5 2.5 0 116 3.5a2.5 2.5 0 010 5z"/></svg><span style="margin-left:4px;line-height:10.4px">48 Cedar Lane<br>Lakeview B.C<br>Canada V2B4DF</span></div>
  </div>
</footer>

<div class="abs bottombar">Copyright © 2015 Northgate Health Group. All Rights Reserved Terms of Use &nbsp;|&nbsp; Privacy Policy &nbsp;|&nbsp; Sitemap</div>

</body>
</html>
```